依頼詳細
ニュースレターのリニューアルに伴う「ニュースレターのテンプレート」作成をお願いします。
下記の「最終成果物」と「必須掲載項目」を満たしていれば、デザインやレイアウトは問いません。お任せいたします。

【最終成果物】
納品は「InDesign」ファイルでお願いします。

サイズ:A4 中綴じ(左開き)横書き

希望する納品物は次の2点です。
1.表紙
2.見開き2ページ(表紙のあとのP2~P3)

下記、必須掲載項目のうち、2~9は納品後テキストや画像の変更を想定しています。
編集可能な状態で作成してください。

【必須掲載項目】
以下は「表紙」と「見開き2ページ」で必ず入れていただきたい項目と挿入するテキストになります。
各項目のデザイン、レイアウト(ページ数以外)はお任せいたします。

必須掲載項目は添付ファイル「必須掲載項目.pdf」にもまとめてあります。ご参照ください。

≪ 表紙 ≫
1. タイトル
挿入テキスト:Harbor insight Bulletin

2. サブタイトル
挿入テキスト:WEB起業家に送る、思考の実践情報。”キーワードをせいするもの、ネットを制す”

3. 号数
挿入テキスト:150号

4. 発行年月
挿入テキスト:2022年12月

5. 特集見出し
挿入テキスト:特集
※ サンプルでハイライトに該当する部分になります。
※ 見出しは2件掲載する予定です。テキストの分量はサンプルと同程度を想定してください。

6. 巻頭言タイトル
挿入テキスト:巻頭言

7. 筆者顔写真
挿入画像:ファイル「筆者写真.png」

8. ページ数(フッター)
挿入テキスト:該当ページ数 Harbor insight 号数(例:1 Harbor insight 150号)
※ レイアウトは左寄せにしてください。

≪見開き2ページ≫
9. ページ数(フッター)
挿入テキスト:該当ページ数 Harbor insight 号数(例:2 Harbor insight 150号)
※ 表紙のフッターからの連番になります。
※ 2ページ(右側ページ)は右寄せ、3ページ(左側ページ)は左寄せにレイアウトしてください。
記載項目
・色はコーポレートカラーの HI DEEP BLUE(RGB:R:0 G:0 B:192、#0000c0)をベースにHI RED PURPLE(RGB: R:230 G:0 B:255、#e600ff)を使用してください。
※ コーポレートカラーの詳細は添付ファイル「必須掲載項目.pdf」をご参照ください。

イメージ、配色などは弊社HPをご参照ください。
https://www.hbi-example.co.jp/

参考として弊社ロゴデータを添付いたします。ご参照ください(ファイル名:harborinsight_logo.zip)

・ニュースレターはデータと印刷両方で配布いたします。カラーで作成していただきたいですが、印刷時はモノクロになることを考慮したデザインにしていただければと思います。

・フォントは有料フォントは使用せず、Adobeでダウンロード可能なものをご使用ください。

・サンプルとして現在仕様しているテンプレートで作成したニュースレターを添付いたします。(ファイル名:Sample.pdf)
希望イメージ
シンプル 複雑
単色 カラフル
暗い 明るい
日常 高級
遊び心 厳粛
未来的 伝統的
女性的 男性的
希望する色
コーポレートカラーをベースに。カラーコードは添付を参照下さい
補足説明
最終納品はInDesign形式でお願いします。
依頼詳細の【必須掲載項目】のうち、8と9の記載内容に誤りがありましたので、
訂正させていただきます。大変失礼いたしました。

誤)
8. ページ数(フッター)
※ レイアウトは左寄せにしてください。

正)
8. ページ数(フッター)
※ レイアウトは右寄せにしてください。

誤)
9. ページ数(フッター)
※ 表紙のフッターからの連番になります。

正)
9. ページ数(フッター)
※ 表紙のフッターからの連番になります。
※ 2ページ(左側ページ)は左寄せ、3ページ(右側側ページ)は右寄せにレイアウトしてください。

(※ 添付の指示書も誤った内容となっています。お手数ですがこちらの訂正をご参照ください。)

既にご提案いただいている方のうち、当初の指示に従って作成していただいている方については、
再提案いただく必要はございません。
採用となった場合、修正の相談をさせていただければと思います。
■ 選んだ理由

コンセプトとこちらの希望をよくご理解いただき、イメージ通りのデザインだったため選ばせていただきました。

■ 提案者全員のお礼・コメント

このたびはご提案いただきありがとうございました。

皆さん弊社のHPを読み込んでくださったり、
コンセプト実現のためのアイデアをご提案いただいたり、
よいご提案ばかりで選ぶのにお時間をいただいてしまいました。

またデザイン関連で必要が生じたときはワークモールで公募したいと思います。
その際はぜひご応募いただければ幸いです。

```html
<!DOCTYPE html>
<html lang="ja">
<head>
<meta charset="utf-8">
<title>Harbor insight Bulletin 150号</title>
<link rel="stylesheet" href="https://fonts.googleapis.com/css2?family=Noto+Sans+JP:wght@400;500;700;900&family=Cormorant+Garamond:wght@400;500&display=swap">
<style>
  :root {
    --deep-blue: #0000c0;
    --red-purple: #e600ff;
    --ink: #2a2a35;
    --rule: #9aa0c8;
    --paper: #ffffff;
    --photo-portrait: linear-gradient(160deg, #6f6a66, #2f2b2a 70%, #4a4440);
    --photo-hall: linear-gradient(180deg, #d7d5d0, #a8a49d 55%, #6e6d6e);
    --photo-lobby: linear-gradient(180deg, #2b2a2c, #5a5550 45%, #b9b1a5 75%, #d8d2c8);
  }
  * { margin: 0; padding: 0; box-sizing: border-box; }
  html, body { width: 846px; height: 1200px; overflow: hidden; background: var(--paper); }
  body { font-family: "Noto Sans JP", sans-serif; color: var(--ink); position: relative; }

  .tagline-band {
    position: absolute; left: 0; top: 0; width: 846px; height: 40px;
    background: var(--deep-blue); color: #fff;
    font-size: 15px; font-weight: 500; letter-spacing: 0.03em;
    display: flex; align-items: center; justify-content: center;
  }

  .brand-square { position: absolute; left: 44px; top: 64px; width: 52px; height: 52px; background: var(--red-purple); }

  .feature { position: absolute; top: 60px; display: flex; gap: 8px; color: var(--deep-blue); }
  .feature svg { flex: none; margin-top: 4px; }
  .feature p { font-size: 19px; font-weight: 900; line-height: 1.5; letter-spacing: 0.01em; }
  .feature--one { left: 140px; width: 318px; }
  .feature--two { left: 492px; width: 320px; }
  .feature-divider { position: absolute; left: 474px; top: 62px; width: 1px; height: 72px; background: var(--rule); }

  .masthead { position: absolute; left: 44px; right: 44px; top: 146px; height: 48px; border-bottom: 1px solid var(--deep-blue);
    display: flex; justify-content: space-between; align-items: flex-end; padding-bottom: 6px; color: var(--deep-blue); }
  .masthead-name { font-weight: 700; font-size: 32px; line-height: 1; letter-spacing: 0.01em; }
  .masthead-issue { font-size: 14px; font-weight: 500; }

  .newsletter-title { position: absolute; left: 44px; right: 44px; top: 200px; height: 96px; border-bottom: 1px solid var(--deep-blue);
    text-align: center; font-family: "Cormorant Garamond", serif; font-weight: 400; font-size: 88px; line-height: 96px;
    letter-spacing: 0.06em; color: var(--deep-blue); }

  .foreword-heading { position: absolute; left: 0; width: 846px; top: 312px; text-align: center;
    font-size: 25px; font-weight: 700; letter-spacing: 0.12em; color: var(--deep-blue); }
  .foreword-heading::after { content: ""; display: block; width: 120px; height: 2px; background: var(--red-purple); margin: 8px auto 0; }

  .foreword { position: absolute; top: 394px; font-size: 13.5px; line-height: 24px; letter-spacing: 0.03em; text-align: justify; }
  .foreword--left { left: 48px; width: 367px; }
  .foreword--right { left: 437px; width: 361px; }
  .author-photo { float: left; width: 160px; height: 150px; margin: 4px 14px 8px 0; background: var(--photo-portrait); }

  .photo { position: absolute; }
  .photo--hall { left: 48px; top: 722px; width: 367px; height: 320px; background: var(--photo-hall); }
  .photo--lobby { left: 437px; top: 722px; width: 361px; height: 392px; background: var(--photo-lobby); }
  .photo-caption { position: absolute; left: 48px; top: 1050px; width: 367px; font-size: 11.5px; line-height: 18px; letter-spacing: 0.02em; }
  .photo-caption--vertical { position: absolute; left: 700px; top: 740px; height: 330px; writing-mode: vertical-rl;
    color: #fff; font-size: 12px; line-height: 19px; letter-spacing: 0.04em; }

  .page-footer { position: absolute; left: 44px; right: 48px; top: 1148px; display: flex; justify-content: flex-end; align-items: baseline; gap: 10px;
    font-size: 13px; color: var(--deep-blue); letter-spacing: 0.02em; padding-top: 8px; border-top: 1px solid var(--rule); }
  .page-footer .page-number { font-weight: 700; color: var(--red-purple); font-size: 15px; }
</style>
</head>
<body>
  <header class="tagline-band">WEB起業家に送る、思考の実践情報。”キーワードをせいするもの、ネットを制す”</header>

  <div class="brand-square" aria-hidden="true"></div>

  <div class="feature feature--one">
    <svg width="22" height="20" viewBox="0 0 22 20"><path d="M2 10 L8 16 L20 3" fill="none" stroke="var(--red-purple)" stroke-width="4" stroke-linecap="round" stroke-linejoin="round"/></svg>
    <p>新人・未経験を半年で１人前にする「手作り研修」の絶大な効果</p>
  </div>
  <div class="feature-divider"></div>
  <div class="feature feature--two">
    <svg width="22" height="20" viewBox="0 0 22 20"><path d="M2 10 L8 16 L20 3" fill="none" stroke="var(--red-purple)" stroke-width="4" stroke-linecap="round" stroke-linejoin="round"/></svg>
    <p>なぜ集客が失敗するのか？<br>検索連動型広告だけではない！<br>集客で成功する思考と戦略</p>
  </div>

  <div class="masthead">
    <span class="masthead-name">Harbor insight Bulletin</span>
    <span class="masthead-issue">2022年12月 150号</span>
  </div>

  <h1 class="newsletter-title">NEWSLETTER</h1>

  <h2 class="foreword-heading">巻頭言</h2>

  <section class="foreword foreword--left">
    <div class="author-photo" role="img" aria-label="筆者の顔写真"></div>
    <p>ハーバーインサイト 水野です。さて、2022年も早くも暮れを迎えました。私たちハーバーインサイトもいよいよ人員が50名を突破しそうで、3年ほどいた港南区のオフィスから徒歩7〜8分の場所に引っ越しをいたします。引っ越しの理由はもちろん、人員を東京で70名、他拠点30名の在籍が可能なまとまったスペースの確保です。</p>
  </section>

  <section class="foreword foreword--right">
    <p>それ以外にも、外部スペースや会議室を増やし、また周囲の環境を緑が多い公園のそばにしたりと、現在のオフィス課題を一掃する今回の引っ越しになりました。それにしても8年前に入居した時の新築の状態を思い出します。「すべての仕事は準備で決まる」という言葉は社内の合言葉です。会員の皆様により良いサービスをご提供できるよう、社員一丸となって精進して参ります。</p>
  </section>

  <div class="photo photo--hall" role="img" aria-label="新オフィス入居ビルのエレベーターホールの写真"></div>
  <p class="photo-caption">入居するビルのエレベーターホール。明るくゆったりとしたスペースで、来客の方を迎える場所です。会議室や共用部も広く、快適に利用できます。</p>

  <div class="photo photo--lobby" role="img" aria-label="新オフィスのエントランスロビーの写真"></div>
  <p class="photo-caption--vertical">エントランスは落ち着いた照明と<br>上質な床材で、迎える空間を演出。<br>デザインにもこだわりました。</p>

  <footer class="page-footer">
    <span class="page-number">1</span>
    <span>Harbor insight</span>
    <span>150号</span>
  </footer>
</body>
</html>
```